KOVlane stands for Kestrel & Ordway venture technologies and specialises in process automation

We are a New company called KOVlane (Kestrel & Ordway venture technologies) a Brisbane based company speciallising in Process Automation for the oil and Gas industry in Australia. We work on projects for DCS, RTU and PLC automation this involves programming and commissioning. We initially need a Website that customers can see about the company and make enquiries. We currently have Royal Blue and grey as our colours on our email signatures but are open for suggestions. Keywords i would suggest yo to look at for insperation are CSG ( coalseam gas) DCS (Distributed control system) RTU (remote terminal unit) and PLC (programmable logic controller).

Target Market(s)

Large CSG companies in Australia, Marlow, Telmar, WXJ, Bendle

Industry/Entity Type

Industry

```html
<!DOCTYPE html>
<html lang="en">
<head>
<meta charset="utf-8">
<title>KOVlane — Process Automation</title>
<link rel="stylesheet" href="https://fonts.googleapis.com/css2?family=Montserrat:wght@400;500;600;700&family=Arimo:wght@400;700&display=swap">
<style>
  :root {
    --navy-deep: #0a1444;
    --navy: #14246a;
    --navy-glow: #22378a;
    --royal: #1d2d86;
    --footer: #060c2c;
    --panel: #f2f2f2;
    --white: #ffffff;
    --ink: #3f3f3f;
    --grey-text: #6d6d6d;
    --grey-light: #b9b9b9;
    --lilac: #8f9de0;
    --footer-text: #b3b8cf;
    --button-dark: #2f2f2f;
  }
  * { box-sizing: border-box; margin: 0; padding: 0; }
  html, body { width: 1200px; height: 1002px; overflow: hidden; }
  body {
    position: relative;
    font-family: "Arimo", Arial, sans-serif;
    background:
      radial-gradient(ellipse 700px 420px at 560px 120px, var(--navy-glow) 0%, transparent 70%),
      linear-gradient(180deg, var(--navy) 0%, var(--navy-deep) 100%);
  }
  .brand { position: absolute; left: 94px; top: 30px; color: var(--white); }
  .brand-name { font-family: "Montserrat", sans-serif; font-weight: 600; font-size: 50px; letter-spacing: -0.5px; line-height: 1; }
  .brand-tagline { margin-top: 10px; font-size: 14px; color: #d6dbf0; }

  .search { position: absolute; left: 837px; top: 52px; width: 269px; height: 36px; background: var(--white); border-radius: 3px; box-shadow: 0 1px 3px rgba(0,0,0,.4); }
  .search-field { position: absolute; left: 14px; top: 11px; font-size: 13px; color: #7a7a7a; }
  .search-button { position: absolute; right: 4px; top: 5px; width: 26px; height: 24px; border-radius: 3px; background: linear-gradient(#3b6ee8, #1d3db5); }
  .search-button svg { position: absolute; left: 5px; top: 4px; }

  .main-panel { position: absolute; left: 94px; top: 136px; width: 1012px; height: 497px; background: var(--panel); border-radius: 3px; box-shadow: 0 4px 14px rgba(0,0,0,.45); }
  .nav { position: absolute; left: 9px; top: 19px; display: flex; align-items: center; gap: 0; }
  .nav-item { font-family: "Montserrat", sans-serif; font-size: 13px; letter-spacing: .6px; color: #3a3a3a; padding: 8px 16px; margin-right: 12px; border-radius: 3px; }
  .nav-item.is-active { background: var(--royal); color: var(--white); }
  .nav-email { position: absolute; right: 10px; top: 22px; display: flex; align-items: center; gap: 8px; font-family: "Montserrat", sans-serif; font-size: 15px; color: #7d7d7d; }

  .hero { position: absolute; left: 9px; top: 69px; width: 993px; height: 418px; background: var(--white); border-radius: 3px; overflow: hidden; }
  .hero-photo { position: absolute; left: 446px; top: 0; width: 547px; height: 418px; background: linear-gradient(100deg, #d9dde2 0%, #8b939c 35%, #5f6872 60%, #3e4650 100%); }
  .hero-fade { position: absolute; left: 420px; top: 0; width: 90px; height: 418px; background: linear-gradient(90deg, #fff 20%, rgba(255,255,255,0)); }
  .hero-title { position: absolute; left: 34px; top: 58px; font-family: "Montserrat", sans-serif; font-weight: 500; font-size: 22px; color: var(--royal); }
  .hero-copy { position: absolute; left: 34px; top: 96px; width: 331px; font-size: 13px; line-height: 22.7px; color: var(--ink); text-align: justify; }
  .hero-button { position: absolute; left: 34px; top: 276px; width: 102px; height: 37px; border-radius: 3px; background: linear-gradient(#4a4a4a, var(--button-dark)); color: var(--white); font-weight: 700; font-size: 14px; display: flex; align-items: center; justify-content: center; box-shadow: 0 1px 2px rgba(0,0,0,.4); }
  .hero-arrows { position: absolute; left: 34px; top: 357px; display: flex; gap: 4px; }
  .hero-arrow { width: 29px; height: 29px; border-radius: 50%; background: linear-gradient(#fafafa, #d8d8d8); border: 1px solid #bdbdbd; display: flex; align-items: center; justify-content: center; }

  .service { position: absolute; top: 680px; width: 242px; }
  .service-head { display: flex; align-items: center; gap: 18px; height: 46px; padding-left: 10px; }
  .service-code { font-family: "Montserrat", sans-serif; font-weight: 700; font-size: 29px; color: var(--white); }
  .service-name { font-size: 14px; line-height: 20px; color: var(--lilac); }
  .service-photo { margin-top: 5px; height: 132px; border: 2px solid #0c1640; box-shadow: 0 3px 8px rgba(0,0,0,.6); }
  .service-reflection { height: 46px; opacity: .22; background: linear-gradient(180deg, #6c7fc0, transparent); }
  .service-csg { left: 94px; } .service-csg .service-photo { background: linear-gradient(160deg, #3e5fa8, #283c74 55%, #c99a4e); }
  .service-dcs { left: 351px; } .service-dcs .service-photo { background: linear-gradient(160deg, #9ab4c6, #4e6474 60%, #2a3440); }
  .service-rtu { left: 607px; } .service-rtu .service-photo { background: linear-gradient(180deg, #6d9ed8, #4c6b45 55%, #8aa35a); }
  .service-plc { left: 864px; } .service-plc .service-photo { background: linear-gradient(170deg, #e6e8ea, #b9bec2 60%, #8a9aa2); }

  .footer { position: absolute; left: 0; top: 919px; width: 1200px; height: 83px; background: var(--footer); }
  .footer-links { position: absolute; left: 94px; top: 20px; font-size: 12px; color: var(--footer-text); word-spacing: 1px; }
  .footer-links span { margin: 0 8px; }
  .footer-copy { position: absolute; left: 94px; top: 51px; font-size: 12px; color: #8a8fa8; word-spacing: 3px; }
  .footer-social { position: absolute; left: 1052px; top: 31px; display: flex; gap: 6px; }
  .social-square { width: 24px; height: 24px; border-radius: 4px; background: #5b79c4; }
</style>
</head>
<body>
  <header class="brand">
    <div class="brand-name">KOVlane</div>
    <div class="brand-tagline">Kestrel &amp; Ordway venture technologies</div>
  </header>

  <div class="search">
    <span class="search-field">Search</span>
    <span class="search-button">
      <svg width="16" height="16" viewBox="0 0 16 16"><circle cx="6.5" cy="6.5" r="4.3" fill="none" stroke="#fff" stroke-width="2"/><line x1="9.8" y1="9.8" x2="14" y2="14" stroke="#fff" stroke-width="2.4" stroke-linecap="round"/></svg>
    </span>
  </div>

  <section class="main-panel">
    <nav class="nav">
      <span class="nav-item is-active">HOME</span>
      <span class="nav-item">ABOUT US</span>
      <span class="nav-item">SERVICES</span>
      <span class="nav-item">OUR WORKS</span>
      <span class="nav-item">CONTACT US</span>
    </nav>
    <div class="nav-email">
      <svg width="28" height="18" viewBox="0 0 28 18"><rect x="1" y="1" width="26" height="16" fill="#a9a9a9"/><polyline points="1,1 14,11 27,1" fill="none" stroke="#f2f2f2" stroke-width="1.5"/></svg>
      <span>E-Mail : info@kovlane.com</span>
    </div>

    <div class="hero">
      <div class="hero-photo" role="img" aria-label="Technician's hand adjusting equipment in a server rack"></div>
      <div class="hero-fade"></div>
      <h1 class="hero-title">Welcome to KOVlane</h1>
      <p class="hero-copy">Pellentesque ipsum purus, accumsan ut nibh non, fringilla tristique metus. Donec venenatis elementum tellus, at aliquet lorem mollis in. Morbi quis vehicula augue, vitae ornare sem. In imperdiet volutpat velit ut aliquet. Donec id ipsum ac elit adipiscing feugiat id quis augue. Nullam commodo neque quis nunc auctor faucibus. Quisque tincidunt volutpat pretium.</p>
      <span class="hero-button">Learn more</span>
      <div class="hero-arrows">
        <span class="hero-arrow"><svg width="10" height="12" viewBox="0 0 10 12"><polyline points="7,1 2,6 7,11" fill="none" stroke="#222" stroke-width="2.6"/></svg></span>
        <span class="hero-arrow"><svg width="10" height="12" viewBox="0 0 10 12"><polyline points="3,1 8,6 3,11" fill="none" stroke="#222" stroke-width="2.6"/></svg></span>
      </div>
    </div>
  </section>

  <article class="service service-csg">
    <div class="service-head"><span class="service-code">CSG</span><span class="service-name">Coalseam Gas</span></div>
    <div class="service-photo" role="img" aria-label="Field workers in hard hats at a gas wellhead"></div>
    <div class="service-reflection"></div>
  </article>
  <article class="service service-dcs">
    <div class="service-head"><span class="service-code">DCS</span><span class="service-name">Distributed Control<br>System</span></div>
    <div class="service-photo" role="img" aria-label="Operator at a control room workstation"></div>
    <div class="service-reflection"></div>
  </article>
  <article class="service service-rtu">
    <div class="service-head"><span class="service-code">RTU</span><span class="service-name">Remote Terminal Unit</span></div>
    <div class="service-photo" role="img" aria-label="Electrical substation in a mountain valley"></div>
    <div class="service-reflection"></div>
  </article>
  <article class="service service-plc">
    <div class="service-head"><span class="service-code">PLC</span><span class="service-name">Programmable Logic<br>Controller</span></div>
    <div class="service-photo" role="img" aria-label="Range of modular programmable logic controller units"></div>
    <div class="service-reflection"></div>
  </article>

  <footer class="footer">
    <div class="footer-links">Home<span>|</span>About us<span>|</span>Services<span>|</span>Our Works<span>|</span>Contact us</div>
    <div class="footer-copy">Copyright © 2013 KOVlane. All rights reserved.</div>
    <div class="footer-social">
      <span class="social-square" role="img" aria-label="Social link"></span>
      <span class="social-square" role="img" aria-label="Social link"></span>
    </div>
  </footer>
</body>
</html>
```